Flyer for annual KESTREL SUMMIT 2020

I would like a church event flyer designed. The event is called "KESTREL SUMMIT 2020". I am looking for a professional, yet catchy design that uses our brand colors and logo creatively while communicating key information of the event effectively.

1. The logo is attached in two color formats. The designer has the choice to use them as he/she want.

2. The location of the event is: Harlow Community Center, 239 Fennimore Street, Portland, ME 04117

3. Time and date of event. The designer can organize and format the date and time as he/she pleases.
Thursday December 31st @ 6:30PM
Friday January 1st @ 6:30PM
Saturday 2nd @ 6:30PM
Sunday 3rd @ 4:30PM

4. The topic of the event is "In Fire and On Fire". The designer is free to use this phrase as he/she pleases to create a good composition.

5. Speaker: Prophet Marcus Olunde (2 pictures of the speaker to choose from are attached)

6. Contact information: contact@brightmeadowfold.org - Telephone number: 207 583 2914

7. I would also like the following three words on the flyer. These words describe the focus of the event: FIRE, REVIVAL, PROPHETIC

Target Market(s)

Young adults

Font styles to use
Sans Serif

Requirements
Must have
• Logo, speaker's picture
Should not have
• cross image, church image

```html
<!DOCTYPE html>
<html lang="en">
<head>
<meta charset="utf-8">
<title>Kestrel Summit 2020 Flyer</title>
<link href="https://fonts.googleapis.com/css2?family=Montserrat:wght@400;500;600;700;800&display=swap" rel="stylesheet">
<style>
  :root {
    --orange: #f7941d;
    --navy: #0e3a5f;
    --panel: #173a64;
    --white: #ffffff;
    --ember-dark: #3a2418;
    --ember-mid: #8a3a1c;
    --ember-hot: #e8641e;
  }
  html, body { margin: 0; padding: 0; overflow: hidden; background: #3d3d3d; }
  .flyer {
    position: relative;
    width: 849px; height: 1200px;
    overflow: hidden;
    font-family: "Montserrat", sans-serif;
    color: var(--white);
  }
  .backdrop {
    position: absolute; inset: 0;
    background:
      radial-gradient(ellipse at 78% 18%, #f39a3a 0%, rgba(232,100,30,0.75) 22%, rgba(138,58,28,0) 55%),
      radial-gradient(ellipse at 85% 75%, rgba(120,90,160,0.55) 0%, rgba(60,40,80,0) 50%),
      linear-gradient(160deg, var(--ember-dark) 0%, #4a2a1c 45%, var(--ember-mid) 100%);
  }
  .speaker-photo {
    position: absolute; left: 0; top: 195px; width: 400px; height: 860px;
    background: linear-gradient(180deg, rgba(40,28,22,0.0) 0%, rgba(220,90,70,0.55) 40%, rgba(210,80,60,0.75) 100%);
    border-radius: 180px 180px 0 0;
  }
  .event-title { position: absolute; left: 47px; top: 70px; width: 330px; text-align: center; }
  .event-title .name { font-weight: 700; font-size: 66px; line-height: 1; color: var(--orange); letter-spacing: 1px; margin: 0; }
  .event-title .edition { font-weight: 600; font-size: 33px; line-height: 1; margin-top: 10px; letter-spacing: 0.5px; }
  .theme { position: absolute; left: 420px; top: 76px; width: 382px; text-align: center; font-weight: 800; font-size: 51px; line-height: 52px; margin: 0; }
  .info-panel {
    position: absolute; left: 398px; top: 275px; width: 423px; height: 584px;
    background: var(--panel); border-radius: 14px;
  }
  .focus { position: absolute; top: 52px; left: 0; right: 0; text-align: center; font-weight: 600; font-size: 19px; letter-spacing: 0.5px; }
  .schedule { position: absolute; top: 155px; left: 0; right: 0; height: 178px; }
  .day { position: absolute; top: 12px; width: 150px; text-align: center; }
  .day .month { font-weight: 500; font-size: 29px; line-height: 32px; }
  .day .date { font-weight: 700; font-size: 104px; line-height: 86px; color: var(--orange); letter-spacing: -3px; margin-top: 6px; }
  .day .time { font-weight: 700; font-size: 18px; margin-top: 10px; }
  .day-1 { left: -7px; } .day-2 { left: 137px; } .day-3 { left: 279px; }
  .divider { position: absolute; top: 0; width: 2px; height: 178px; background: var(--white); }
  .divider-1 { left: 134px; } .divider-2 { left: 288px; }
  .venue { position: absolute; left: 18px; top: 424px; font-weight: 500; font-size: 18px; line-height: 24px; color: var(--orange); }
  .contact { position: absolute; left: 21px; top: 489px; font-size: 17px; line-height: 24px; }
  .contact .label { font-weight: 500; font-size: 18px; }
  .contact .detail { font-weight: 400; }
  .footer-band { position: absolute; left: 0; top: 0; }
  .speaker-name { position: absolute; left: 52px; top: 1118px; font-weight: 700; font-size: 30px; letter-spacing: 0.5px; margin: 0; }
  .brand { position: absolute; left: 560px; top: 1090px; display: flex; align-items: center; gap: 12px; }
  .brand .dot { width: 22px; height: 22px; border-radius: 50%; background: var(--orange); }
  .brand .wordmark { font-weight: 600; font-size: 40px; letter-spacing: 1px; color: var(--white); }
</style>
</head>
<body>
<main class="flyer">
  <div class="backdrop" role="img" aria-label="Background photograph of orange and violet flames and smoke"></div>
  <div class="speaker-photo" role="img" aria-label="Portrait photograph of the speaker in a coral blazer and dark tie"></div>

  <header class="event-title">
    <h1 class="name">KESTREL</h1>
    <div class="edition">SUMMIT 2020</div>
  </header>

  <h2 class="theme">IN FIRE AND<br>ON FIRE</h2>

  <section class="info-panel">
    <div class="focus">FIRE | REVIVAL | PROPHETIC</div>
    <div class="schedule">
      <div class="day day-1"><div class="month">DEC</div><div class="date">31</div><div class="time">@ 6:30 pm</div></div>
      <span class="divider divider-1"></span>
      <div class="day day-2"><div class="month">JAN</div><div class="date">1,2</div><div class="time">@ 6:30 pm</div></div>
      <span class="divider divider-2"></span>
      <div class="day day-3"><div class="month">JAN</div><div class="date">3</div><div class="time">@ 4:30 pm</div></div>
    </div>
    <address class="venue" style="font-style:normal">Harlow Community Center,<br>239 Fennimore Street, Portland, ME 04117</address>
    <div class="contact">
      <div class="label">Contact information</div>
      <div class="detail">contact@brightmeadowfold.org</div>
      <div class="detail">Telephone number: 207 583 2914</div>
    </div>
  </section>

  <svg class="footer-band" width="849" height="1200" viewBox="0 0 849 1200" aria-hidden="true">
    <polygon points="0,914 424,1040 849,879 849,905 424,1062 0,942" fill="#ffffff"/>
    <polygon points="0,942 424,1062 849,905 849,1200 0,1200" fill="#0e3a5f"/>
  </svg>

  <h3 class="speaker-name">PROPHET MARCUS OLUNDE</h3>

  <div class="brand">
    <span class="dot"></span>
    <span class="wordmark">VANTREL</span>
  </div>
</main>
</body>
</html>
```